Business Card Design Project

We need a redesign of our business card.
We are a Consulting Property Developer called The Kestrel Group
Updates

Thank you all for submissions. Just waiting on managment to decide.

Thank you,

Dorinda

Industry/Entity Type

Business

Requirements
Must have
• we like having the KG a focus in the back ground or on the side
Kestrel is our company colour

the wording - property development
and - premium accommodation

our website www.kestrelgroup-example.com.au

persons name
title

p: 1300 482917 f: 1300 482915 m: 0417593824
PO Box 5817, Brindlevale Qld 4178
e: admin@kestrelgroup-example.com.au

```html
<!DOCTYPE html>
<html lang="en">
<head>
<meta charset="utf-8">
<title>The Kestrel Group – Business Card</title>
<link href="https://fonts.googleapis.com/css2?family=Open+Sans:wght@400&family=Crimson+Text:wght@400&display=swap" rel="stylesheet">
<style>
  :root {
    --page: #ffffff;
    --card: #050505;
    --kestrel: #9a1f26;
    --kestrel-dark: #5a0608;
    --silver-light: #e6e6e6;
    --silver-mid: #bdbdbd;
    --silver-dark: #8a8a8a;
    --text-light: #e9e9e9;
    --text-muted: #c8c8c8;
  }
  * { margin: 0; padding: 0; box-sizing: border-box; }
  html, body {
    width: 1200px; height: 900px; overflow: hidden;
    background: var(--page);
  }
  .canvas {
    position: relative; width: 1200px; height: 900px;
  }
  .card {
    position: absolute;
    width: 700px; height: 400px;
    background: var(--card);
    border-radius: 40px;
    overflow: hidden;
    box-shadow: 0 6px 18px rgba(0,0,0,0.25);
  }
  .card--front { left: 250px; top: 35px; }
  .card--back  { left: 250px; top: 465px; }

  .brand {
    position: absolute;
    display: flex; align-items: center; gap: 14px;
    font-family: "Open Sans", sans-serif;
    font-size: 36px;
    color: var(--text-muted);
    letter-spacing: 0.5px;
    white-space: nowrap;
  }
  .brand__mark {
    width: 26px; height: 26px; border-radius: 50%;
    background: var(--kestrel);
  }
  .brand-rule {
    position: absolute; height: 1px; background: var(--silver-dark);
  }
  .card--front .brand { left: 130px; top: 40px; }
  .card--front .brand-rule { left: 120px; top: 98px; width: 440px; }

  .accent-circle {
    position: absolute; right: 40px; top: 10px;
    width: 150px; height: 150px; border-radius: 50%;
    background: rgba(120,120,120,0.28);
  }

  .person {
    position: absolute; left: 60px; top: 215px;
    font-family: "Crimson Text", serif;
  }
  .person__name { font-size: 27px; color: var(--text-light); }
  .person__title { font-size: 22px; color: var(--kestrel); margin-top: 2px; }

  .contact {
    position: absolute; left: 400px; top: 120px;
    font-family: "Crimson Text", serif;
    font-size: 16px; line-height: 21px;
    color: var(--text-muted);
    list-style: none;
  }

  .card--front .red-line {
    position: absolute; left: 0; right: 0; top: 300px;
    height: 2px; background: var(--kestrel);
  }
  .silver-band {
    position: absolute; left: 0; right: 0; top: 312px; height: 88px;
    background: linear-gradient(90deg, var(--silver-dark), var(--silver-light) 45%, var(--silver-mid) 80%, var(--silver-dark));
  }
  .web {
    position: absolute; left: 0; right: 0;
    text-align: center;
    font-family: "Crimson Text", serif;
    font-size: 22px; letter-spacing: 0.5px;
  }
  .silver-band .web { top: 14px; color: var(--kestrel); }

  .card--back .brand { left: 0; right: 0; top: 120px; justify-content: center; }
  .card--back .brand-rule { left: 150px; top: 178px; width: 420px; }
  .card--back .silver-line {
    position: absolute; left: 0; right: 0; top: 262px; height: 3px;
    background: linear-gradient(90deg, var(--silver-dark), var(--silver-light) 60%, var(--silver-dark));
  }
  .kestrel-band {
    position: absolute; left: 0; right: 0; top: 278px; height: 122px;
    background: linear-gradient(90deg, var(--kestrel-dark), var(--kestrel) 40%, var(--kestrel) 70%, var(--kestrel-dark));
  }
  .kestrel-band .web { top: 40px; color: var(--text-muted); }
</style>
</head>
<body>
<main class="canvas">
  <section class="card card--front" aria-label="Business card front">
    <div class="accent-circle"></div>
    <div class="brand"><span class="brand__mark"></span><span>The Kestrel Group</span></div>
    <div class="brand-rule"></div>
    <ul class="contact">
      <li>PO Box 5817, Brindlevale Qld 4178</li>
      <li>P : 130-048-2917</li>
      <li>F : 130-048-2915</li>
      <li>M : 0417593824</li>
      <li>E : admin@kestrelgroup-example.com.au</li>
    </ul>
    <div class="person">
      <p class="person__name">Dorinda Harlowe</p>
      <p class="person__title">Title</p>
    </div>
    <div class="red-line"></div>
    <div class="silver-band"><p class="web">www.kestrelgroup-example.com.au</p></div>
  </section>

  <section class="card card--back" aria-label="Business card back">
    <div class="brand"><span class="brand__mark"></span><span>The Kestrel Group</span></div>
    <div class="brand-rule"></div>
    <div class="silver-line"></div>
    <div class="kestrel-band"><p class="web">www.kestrelgroup-example.com.au</p></div>
  </section>
</main>
</body>
</html>
```